Website re-design

We are a successful furnished apartment provider in Boston. We currently are working on re-designing our website www.bexlodging.com to make it more modern, designer look and user friendly. We hired a designer, but are not happy with the designs proposed and want to improve on them. The winning design will be paid regardless of whether we stay with our current designer or not. We want ideas and functional page links to see how it will work. Platform we have chosen is wordpress. Feel free to propose others easy for us to update and modify. We do not like Joomla on which website is currently running. We do not like flash nor long load times.
Please use photos on our website for design presentations. www.bexlodging.com

Target Market(s)

doctors, nurses, business men but mostly business women, some post-medical students

Industry/Entity Type

Apartment

Requirements
Must have
• Quick action button for reservation form and a notification and email forwarding system to us of reservation information by potential clients. Blog required with feedback by guests allowed, we can censor which are published. Slide shows of apartments.
Should not have
• No movies.

```html
<!DOCTYPE html>
<html lang="en">
<head>
<meta charset="utf-8">
<title>Bex Lodging Furnished Apartments</title>
<link rel="stylesheet" href="https://fonts.googleapis.com/css2?family=Cinzel:wght@400;600&display=swap">
<style>
  :root {
    --bg: #3d3f2c;
    --gold: #e9b560;
    --gold-line: #8a6a30;
    --text: #ffffff;
    --dark: #15150c;
    --dot-active: #f4c97a;
    --photo-warm: #d98a3a;
  }
  * { margin: 0; padding: 0; box-sizing: border-box; }
  html, body { width: 1200px; height: 830px; overflow: hidden; background: var(--bg); }
  .page { position: relative; width: 1200px; height: 830px; }

  .brand { position: absolute; left: 150px; top: 18px; width: 130px; text-align: center; }
  .brand-mark { width: 60px; height: 60px; border-radius: 50%; background: var(--gold); margin: 0 auto 8px; }
  .brand-name { font-family: "Cinzel", serif; font-weight: 400; font-size: 17px; color: var(--gold); letter-spacing: 1px; white-space: nowrap; }

  .main-nav { position: absolute; top: 61px; left: 0; }
  .main-nav a { position: absolute; font-family: "Cinzel", serif; font-weight: 600; font-size: 14px; color: var(--gold); text-decoration: none; white-space: nowrap; }

  .rule { position: absolute; left: 143px; width: 914px; height: 1px; background: var(--gold-line); }
  .rule-top { top: 129px; }
  .rule-foot { top: 761px; background: #5e5a3c; }

  .photo { position: absolute; border: 1px solid var(--gold); }
  .photo-side-left { left: 143px; top: 355px; width: 162px; height: 147px; background: linear-gradient(135deg, #c9b8a0, #6a4530 60%, #3a2a22); }
  .photo-main { left: 304px; top: 170px; width: 592px; height: 361px; background: linear-gradient(120deg, #e8a050 0%, var(--photo-warm) 40%, #f2e6d4 65%, #8a4a20 100%); z-index: 2; }
  .photo-side-right { left: 896px; top: 355px; width: 161px; height: 147px; background: linear-gradient(135deg, #8a4a3a, #5a6a3a 55%, #2a2a22); border-color: #cfc8b0; }

  .slider-rule { position: absolute; height: 1px; }
  .slider-rule-upper { left: 304px; top: 546px; width: 592px; background: linear-gradient(90deg, transparent, #6e6440, transparent); }
  .slider-rule-lower { left: 276px; top: 566px; width: 652px; background: linear-gradient(90deg, transparent, var(--gold-line) 20%, var(--gold-line) 80%, transparent); }
  .slider-dots { position: absolute; top: 551px; left: 528px; display: flex; gap: 9px; }
  .slider-dots span { width: 10px; height: 10px; border-radius: 50%; border: 1px solid var(--gold); }
  .slider-dots .is-active { background: var(--dot-active); }

  .welcome { position: absolute; left: 143px; top: 598px; width: 914px; }
  .welcome h1 { font-family: "Cinzel", serif; font-weight: 600; font-size: 24px; color: var(--gold); letter-spacing: 0.3px; margin-bottom: 6px; }
  .welcome p { font-family: Arial, Helvetica, sans-serif; font-size: 13.6px; line-height: 21px; color: var(--text); }
  .welcome a { color: var(--gold); font-weight: bold; text-decoration: none; }

  .contact-line { position: absolute; top: 773px; left: 0; width: 1200px; text-align: center; font-family: "Cinzel", serif; font-weight: 600; font-size: 12.5px; color: var(--gold); }
  .contact-line .sep { margin: 0 8px; }

  .share { position: absolute; top: 795px; left: 500px; display: flex; gap: 12px; }
  .share-item { display: flex; align-items: center; }
  .share-btn { width: 34px; height: 15px; border-radius: 2px; background: #4a66a0; }
  .share-btn.alt { background: #3aa0c8; width: 42px; }
  .share-btn.third { background: #c8c8c8; width: 24px; }
  .share-count { height: 15px; padding: 0 3px; background: #fff; border: 1px solid #aaa; font-family: Arial, sans-serif; font-size: 9px; line-height: 13px; color: #333; }

  .copyright { position: absolute; top: 803px; right: 143px; font-family: "Cinzel", serif; font-size: 10.5px; color: var(--dark); }
</style>
</head>
<body>
<div class="page">
  <header>
    <div class="brand">
      <div class="brand-mark"></div>
      <div class="brand-name">BEX LODGING</div>
    </div>
    <nav class="main-nav">
      <a href="#" style="left:324px">APARTMENTS</a>
      <a href="#" style="left:463px">REVIEW</a>
      <a href="#" style="left:560px">COMMUNITY</a>
      <a href="#" style="left:693px">RESERVATION</a>
      <a href="#" style="left:835px">ABOUT US</a>
      <a href="#" style="left:948px">BLOG</a>
    </nav>
    <div class="rule rule-top"></div>
  </header>

  <section class="slideshow">
    <div class="photo photo-side-left" role="img" aria-label="Apartment living room with armchairs and tall windows"></div>
    <div class="photo photo-main" role="img" aria-label="Bright studio apartment with bed, orange walls and kitchenette"></div>
    <div class="photo photo-side-right" role="img" aria-label="Brick row houses with iron railings in the South End"></div>
    <div class="slider-rule slider-rule-upper"></div>
    <div class="slider-dots">
      <span class="is-active"></span><span></span><span></span><span></span><span></span><span></span><span></span><span></span>
    </div>
    <div class="slider-rule slider-rule-lower"></div>
  </section>

  <section class="welcome">
    <h1>Welcome to Bex Lodging Furnished Apartments</h1>
    <p>Bex Lodging Furnished Apartments is proud to offer some of the best furnished apartments in Boston. Our locations are in the trendiest area of the city: the South End. In the South End neighborhood, you will find wonderful restaurants, theaters, cafes and artist lofts. Our short term and extended stay apartments are very, very clean. We also offer the latest designer layouts: hardwood floors, Wireless Dsl, Cable TV, flat screen in most apartments, washer and dryer, cookware, cotton linens. Please check out photo galleries, pricing, availability and reservation form and <a href="#">contact us</a> for more information.</p>
  </section>

  <footer>
    <div class="rule rule-foot"></div>
    <div class="contact-line">412 Harlow Street, Boston, MA 02118<span class="sep">•</span>617.555.0142<span class="sep">•</span>info@bexlodging.com</div>
    <div class="share">
      <div class="share-item"><span class="share-btn"></span><span class="share-count">1212</span></div>
      <div class="share-item"><span class="share-btn alt"></span><span class="share-count">444</span></div>
      <div class="share-item"><span class="share-btn third"></span><span class="share-count">102</span></div>
    </div>
    <div class="copyright">©2012 Bex Lodging. All Rights Reserved.</div>
  </footer>
</div>
</body>
</html>
```